Dorvelan Swimming & Athletics Center

We need Business Card for a Athletics center
The logo frome the Uploaded Files ( b card fimal)
Οn one side of card we need the logo of company the Contact and the website:
1. Address:(Limassol, Cyprus 12-14 Stavrinelou str,Ano Trimeni,P.C. 4832)

2.Phone number: (+357) 25-704263

3. Mail: info@dorvelanfit.example

3. Website: www.dorvelanfit.example

Οn the other side of the card we need to write the sport of the company:

1. Artistic Gymnastics
2. Swimming
3. Gym - Fitness
4. Programs
5. Dancing
5.Tennis

From the Uploaded Files you can get the logo.In a logo is behind the black color which can be removed from logo.

Υou can use that color you want.
.
Updates

Industry/Entity Type

Business

Font styles to use
Decorative

Colors
0555a3
ffcf3e
3176b5
0692cd
add136
f04a50
000000
cfcfcf
9d9d9d

Requirements
Should not have
• photos with faces
• photo fro the Website:www.dorvelanfit.example

```html
<!DOCTYPE html>
<html lang="en">
<head>
<meta charset="utf-8">
<title>Dorvelan Swimming &amp; Athletics Center – Business Card</title>
<link rel="stylesheet" href="https://fonts.googleapis.com/css2?family=Questrial&display=swap">
<style>
  :root {
    --bg: #e9e6e1;
    --card: #ffffff;
    --orange: #f39a1e;
    --amber: #f7b52c;
    --yellow: #fde24a;
    --navy: #1f2f6b;
    --ink: #3a3a3a;
    --muted: #6a6a6a;
  }
  * { box-sizing: border-box; margin: 0; padding: 0; }
  html, body { width: 1200px; height: 1023px; overflow: hidden; }
  body {
    background: var(--bg);
    font-family: "Questrial", "Century Gothic", sans-serif;
    position: relative;
  }
  .card {
    position: absolute;
    width: 640px;
    height: 370px;
    background: var(--card);
    border-radius: 26px;
    overflow: hidden;
    box-shadow: 0 10px 28px rgba(0,0,0,.18);
  }
  .card--front { left: 70px; top: 60px; }
  .card--back { left: 490px; top: 590px; }

  .brand {
    position: absolute;
    display: flex;
    align-items: center;
    gap: 18px;
  }
  .brand__name {
    color: var(--orange);
    font-size: 64px;
    letter-spacing: 2px;
    line-height: 1;
  }
  .brand__mark {
    width: 62px; height: 62px;
    border-radius: 50%;
    background: var(--yellow);
    flex: none;
  }
  .card--front .brand { left: 40px; top: 42px; }

  .edge-stripe--navy {
    position: absolute; right: 0; top: 0;
    width: 46px; height: 150px; background: var(--navy);
  }
  .edge-stripe--yellow {
    position: absolute; right: 0; top: 206px;
    width: 46px; height: 164px;
    background: linear-gradient(180deg, var(--amber), var(--yellow));
  }
  .name-band {
    position: absolute; left: 0; top: 150px;
    width: 100%; height: 56px;
    background: linear-gradient(90deg, var(--orange), var(--yellow) 60%, var(--amber));
    padding: 8px 40px;
    color: #fff;
  }
  .name-band__name { font-size: 21px; line-height: 1.1; }
  .name-band__role { font-size: 14px; }
  .bottom-stripe {
    position: absolute; left: 0; bottom: 0;
    width: 100%; height: 10px;
    background: linear-gradient(90deg, var(--orange), var(--yellow));
  }

  .contacts {
    position: absolute; left: 40px; top: 228px;
    list-style: none;
    font-size: 15px; color: var(--ink);
  }
  .contacts li { display: flex; align-items: center; gap: 10px; line-height: 26px; }
  .contacts svg { width: 15px; height: 15px; flex: none; }

  .address {
    position: absolute; right: 70px; top: 228px;
    text-align: right;
    font-size: 15px; line-height: 26px; color: var(--ink);
    font-style: normal;
  }

  .card--back .brand {
    left: 0; right: 0; top: 120px;
    justify-content: center;
  }
  .card--back .brand__name { font-size: 72px; }
  .sports {
    position: absolute; left: 0; right: 0; top: 220px;
    text-align: center;
    color: var(--orange);
    font-size: 17px; line-height: 26px;
  }
</style>
</head>
<body>

<section class="card card--front" aria-label="Business card front">
  <div class="brand">
    <span class="brand__name">DORVELAN</span>
    <span class="brand__mark"></span>
  </div>
  <div class="edge-stripe--navy"></div>
  <div class="name-band">
    <p class="name-band__name">Marek Halloran</p>
    <p class="name-band__role">Managing Director</p>
  </div>
  <div class="edge-stripe--yellow"></div>

  <ul class="contacts">
    <li>
      <svg viewBox="0 0 16 16"><rect x="1" y="5" width="14" height="10" rx="2" fill="var(--orange)"/><rect x="4" y="1" width="8" height="5" fill="var(--orange)"/></svg>
      (+357) 25-48 2175
    </li>
    <li>
      <svg viewBox="0 0 16 16"><path d="M3 1l3 3-2 2c1 3 3 5 6 6l2-2 3 3-2 2C6 15 1 10 1 3z" fill="var(--orange)"/></svg>
      (+357) 25-704263
    </li>
    <li>
      <svg viewBox="0 0 16 16"><rect x="1" y="3" width="14" height="10" fill="var(--orange)"/><path d="M1 3l7 6 7-6" stroke="#fff" fill="none" stroke-width="1.4"/></svg>
      info@dorvelanfit.example
    </li>
    <li>
      <svg viewBox="0 0 16 16"><circle cx="8" cy="8" r="7" fill="var(--orange)"/><path d="M1 8h14M8 1c-3 4-3 10 0 14M8 1c3 4 3 10 0 14" stroke="#fff" fill="none" stroke-width="1"/></svg>
      www.dorvelanfit.example
    </li>
  </ul>

  <address class="address">
    Limassol, Cyprus 12-14<br>
    Stavrinelou str,<br>
    Ano Trimeni, P.C. 4832
  </address>
  <div class="bottom-stripe"></div>
</section>

<section class="card card--back" aria-label="Business card back">
  <div class="brand">
    <span class="brand__name">DORVELAN</span>
    <span class="brand__mark"></span>
  </div>
  <p class="sports">
    Artistic Gymnastics, Swimming, Gym - Fitness<br>
    Programs, Dancing, Tennis
  </p>
</section>

</body>
</html>
```